Tour agency for FIT and groups need a business card design

We need a business card design for a tour agency company that is based in Perth called" LUMEN QX", we aim to provide customise, unique and seamless travel arrangement for FIT and groups. We serve both high profile businessperson, government authorities, business partners, executives and investors. The name card should be more professional looking.

Target Market(s)

High profile businessperson, government authorities, business partners, executives and investors.

Industry/Entity Type

Tourism

Contact Information for Business Card

Lumen QX
Level 1, 218 Marbury Crescent, Tallowdale WA, 6015
www.lumenqx.com.au

Font styles to use
Serif

Colors

Designer to choose colors to be used in the design.

Requirements
Must have
• My project must have a company logo
Nice to have
• a more professional and solid yet friendly name card design. We may want to include chinese name in the name card as well. Edge of the card can be filled with gold and we think that transparent name cards are interesting.

```html
<!DOCTYPE html>
<html lang="en">
<head>
<meta charset="utf-8">
<title>Lumen QX — Business Card</title>
<link rel="stylesheet" href="https://fonts.googleapis.com/css2?family=Mulish:wght@300;400&family=Noto+Sans:wght@400&display=swap">
<style>
  :root {
    --page: #ffffff;
    --card: #0a0606;
    --silver: #b9b9b9;
    --ink: #ffffff;
    --rule: #e6e6e6;
  }
  * { margin: 0; padding: 0; box-sizing: border-box; }
  html, body {
    width: 1200px;
    height: 948px;
    overflow: hidden;
    background: var(--page);
  }
  .canvas {
    position: relative;
    width: 1200px;
    height: 948px;
  }
  .card {
    position: absolute;
    left: 261px;
    width: 678px;
    height: 388px;
    background: var(--card);
    border-radius: 44px;
    overflow: hidden;
  }
  .card--front { top: 69px; }
  .card--back { top: 506px; }

  .front-mark {
    position: absolute;
    left: 0;
    right: 0;
    top: 166px;
    text-align: center;
    font-family: "Mulish", sans-serif;
    font-weight: 300;
    font-size: 62px;
    line-height: 1;
    letter-spacing: 1px;
    color: var(--silver);
  }

  .brand,
  .tagline,
  .person-name,
  .person-role {
    position: absolute;
    line-height: 1;
    white-space: nowrap;
  }
  .brand {
    left: 52px;
    top: 54px;
    font-family: "Mulish", sans-serif;
    font-weight: 300;
    font-size: 54px;
    color: var(--silver);
    letter-spacing: -0.5px;
  }
  .tagline {
    left: 58px;
    top: 110px;
    font-family: "Noto Sans", sans-serif;
    font-size: 17px;
    color: var(--ink);
  }
  .person-name {
    left: 57px;
    top: 173px;
    font-family: "Noto Sans", sans-serif;
    font-size: 23px;
    color: var(--ink);
  }
  .person-role {
    left: 58px;
    top: 201px;
    font-family: "Noto Sans", sans-serif;
    font-size: 17px;
    color: var(--ink);
  }
  .divider {
    position: absolute;
    left: 0;
    top: 225px;
    width: 498px;
    height: 1px;
    background: var(--rule);
  }
  .contacts {
    position: absolute;
    left: 59px;
    top: 239px;
    list-style: none;
    font-family: "Noto Sans", sans-serif;
    font-size: 15px;
    color: var(--ink);
  }
  .contacts li {
    display: flex;
    height: 28.5px;
    line-height: 28px;
    white-space: nowrap;
  }
  .contacts .label {
    width: 35px;
    white-space: pre;
  }
</style>
</head>
<body>
<main class="canvas">
  <section class="card card--front">
    <div class="front-mark">Lumen QX</div>
  </section>

  <section class="card card--back">
    <div class="brand">Lumen QX</div>
    <div class="tagline">Travel Consultation Service</div>
    <div class="person-name">Tessa Moray</div>
    <div class="person-role">Administrative Assistant</div>
    <div class="divider"></div>
    <ul class="contacts">
      <li><span class="label">P  :</span><span>+61 (0) 400 555 017</span></li>
      <li><span class="label">E  :</span><span>tessa@lumenqx.com.au</span></li>
      <li><span class="label">W :</span><span>www.lumenqx.com.au</span></li>
      <li><span class="label">A  :</span><span>Level 1, 218 Marbury Crescent, Tallowdale WA, 6015</span></li>
    </ul>
  </section>
</main>
</body>
</html>
```